Unique Playing Card Deck Design

Brief:

I am looking for a designer to design a whole deck of cards from the ground up. I would like both the front and back designed for the deck, and would like the desk to include all the standard cards including jokers. I would like to make each card as unique as possible, so including original designs and artwork for the non-face cards as well.

I would like these cards to be poker size (63mm x 88mm, 2.5" x 3.5") or B8 size according to ISO 216) and I’ve attached a template that should be followed for the sizing.

No real limit on the design so be as creative as you can!

Design Details

Color Mode: RGB or CYMK for color images, Grayscale for black and white

File types: JPG, BMP, PNG, GIF, TIFF

Image resolution: Minimum 300 dpi

Bleeding: Allow 1/8" (approx 36 pixels based on a 300dpi image) for bleeding and a further 1/8" for safe area margin inside each side

EDIT: Because this project requires a lot of design work I am fine for the submissions to be limited to 3 or 4 cards that would demonstrate the overall direction that you are taking. Once I have chosen the designs we can continue refining them and adding the rest of the deck. I would also like a box for the cards to be designed and can provide a template after I have chosen the designers. Thanks and please let me know if you have any questions!

EDIT2: I realize this project is a lot of work and so I have taken the amounts that I had for 2nd and 3rd place and increased the reward for 1st place. I am still interested in selecting multiple designs, but because this project is being done on a committed payment basis I wanted to ensure that I was only obligated to select one design. However, if there are multiple designs that I am interested in, I will award the design work to an additional 1-3 designers (to a maximum of 4 total) on the same terms as 1st place. i.e. all designers selected will be paid the same amount. Thanks again for looking!

Target Market(s)

Adult card players who appreciate good design (i.e. the designs should not be cartoon-like or targeted at children). These are going to be premium cards printed on the best quality paper etc so I would like the design to reflect this.

Font styles to use
Decorative
Script

Requirements
Nice to have
• I will leave the design idea up to you but I like the look of really old playing cards (think of a deck of medieval playing cards for example). I also like the art deco kind of aesthetic. On the complete opposite side of the spectrum a very modern looking, minimalist design is also appealing.
• These are just a few ideas but as I said I am really open to anything. It just needs to be a bold, original design.

```html
<!DOCTYPE html>
<html lang="en">
<head>
<meta charset="utf-8">
<title>Ten of Spades</title>
<link rel="stylesheet" href="https://fonts.googleapis.com/css2?family=Playfair+Display:wght@700&display=swap">
<style>
  :root {
    --card-red: #d13028;
    --ink: #000000;
    --paper: #ffffff;
    --gold: #ffdd44;
    --numeral-font: "Playfair Display", "Bodoni Moda", serif;
  }
  html, body {
    margin: 0;
    padding: 0;
    width: 826px;
    height: 1200px;
    overflow: hidden;
    background: var(--paper);
  }
  .card {
    position: relative;
    width: 826px;
    height: 1200px;
  }
  .card-art {
    position: absolute;
    inset: 0;
  }
  .tile {
    position: absolute;
    box-sizing: border-box;
  }
  .tile--red { background: var(--card-red); }
  .tile--gold { background: var(--gold); }
  .tile--numeral {
    background: var(--ink);
    display: flex;
    align-items: center;
    justify-content: center;
    color: var(--paper);
    font-family: var(--numeral-font);
    font-weight: 700;
    font-size: 128px;
    font-variant-numeric: lining-nums;
    font-feature-settings: "lnum" 1;
    line-height: 1;
    letter-spacing: -5px;
    padding-bottom: 6px;
  }
  .tile--open { background: transparent; }
  .tile--framed { border: 4px solid var(--gold); }
  .emblem {
    position: absolute;
    box-sizing: border-box;
  }
  .emblem--star { background: var(--card-red); }
  .emblem--orbit {
    background: var(--gold);
    border: 4px solid var(--gold);
    outline: 6px solid var(--card-red);
    outline-offset: -14px;
  }
</style>
</head>
<body>
<main class="card">
  <svg class="card-art" width="826" height="1200" viewBox="0 0 826 1200" aria-hidden="true">
    <defs>
      <symbol id="spade" viewBox="0 0 100 110">
        <path d="M50 0 C30 30 0 45 0 68 C0 88 25 95 45 80 C43 95 38 103 30 110 H70 C62 103 57 95 55 80 C75 95 100 88 100 68 C100 45 70 30 50 0Z"/>
      </symbol>
    </defs>
    <rect class="card-face" x="35" y="52" width="755" height="1110" fill="var(--card-red)"/>
    <g class="corner-spades" fill="var(--ink)">
      <use href="#spade" x="72" y="92" width="88" height="96"/>
      <use href="#spade" x="658" y="92" width="88" height="96"/>
      <use href="#spade" x="72" y="1028" width="88" height="96"/>
      <use href="#spade" x="658" y="1028" width="88" height="96"/>
    </g>
    <g class="spade-border spade-border--top" fill="var(--ink)">
      <use href="#spade" x="219" y="84" width="18" height="20"/>
      <use href="#spade" x="250" y="84" width="18" height="20"/>
      <use href="#spade" x="281" y="84" width="18" height="20"/>
      <use href="#spade" x="311" y="84" width="18" height="20"/>
      <use href="#spade" x="342" y="84" width="18" height="20"/>
      <use href="#spade" x="373" y="84" width="18" height="20"/>
      <use href="#spade" x="404" y="84" width="18" height="20"/>
      <use href="#spade" x="434" y="84" width="18" height="20"/>
      <use href="#spade" x="465" y="84" width="18" height="20"/>
      <use href="#spade" x="496" y="84" width="18" height="20"/>
      <use href="#spade" x="527" y="84" width="18" height="20"/>
      <use href="#spade" x="557" y="84" width="18" height="20"/>
      <use href="#spade" x="588" y="84" width="18" height="20"/>
      <use href="#spade" x="619" y="84" width="18" height="20"/>
    </g>
    <g class="spade-border spade-border--bottom" fill="var(--ink)">
      <use href="#spade" x="214" y="1108" width="18" height="20"/>
      <use href="#spade" x="245" y="1108" width="18" height="20"/>
      <use href="#spade" x="276" y="1108" width="18" height="20"/>
      <use href="#spade" x="306" y="1108" width="18" height="20"/>
      <use href="#spade" x="337" y="1108" width="18" height="20"/>
      <use href="#spade" x="368" y="1108" width="18" height="20"/>
      <use href="#spade" x="399" y="1108" width="18" height="20"/>
      <use href="#spade" x="429" y="1108" width="18" height="20"/>
      <use href="#spade" x="460" y="1108" width="18" height="20"/>
      <use href="#spade" x="491" y="1108" width="18" height="20"/>
      <use href="#spade" x="522" y="1108" width="18" height="20"/>
      <use href="#spade" x="552" y="1108" width="18" height="20"/>
      <use href="#spade" x="583" y="1108" width="18" height="20"/>
      <use href="#spade" x="614" y="1108" width="18" height="20"/>
    </g>
    <path class="frame-outer" fill="var(--paper)"
      d="M188 122 H636 A80 80 0 0 0 716 202 V1014 A80 80 0 0 0 636 1094 H188 A80 80 0 0 0 108 1014 V202 A80 80 0 0 0 188 122 Z"/>
    <path class="frame-inner" fill="var(--ink)"
      d="M210 146 H612 A78 78 0 0 0 690 224 V992 A78 78 0 0 0 612 1070 H210 A78 78 0 0 0 132 992 V224 A78 78 0 0 0 210 146 Z"/>
    <polygon class="wedge wedge--top" fill="var(--gold)" points="500,240 536,350 666,382 500,382"/>
    <polygon class="wedge wedge--bottom" fill="var(--gold)" points="150,874 274,910 310,1016 310,874"/>
    <g class="nested-frame">
      <rect x="500" y="714" width="166" height="144" fill="var(--card-red)"/>
      <rect x="520" y="728" width="132" height="118" fill="var(--ink)"/>
      <rect x="526" y="740" width="118" height="92" fill="var(--gold)"/>
      <rect x="538" y="752" width="92" height="68" fill="var(--card-red)"/>
    </g>
  </svg>

  <!-- row 1 -->
  <div class="tile tile--red" style="left:310px;top:240px;width:190px;height:142px"></div>
  <div class="emblem emblem--star" role="img" aria-label="White line ornament of two overlapping squares"
       style="left:352px;top:259px;width:112px;height:112px"></div>
  <div class="tile tile--numeral tile--framed" style="left:148px;top:238px;width:164px;height:148px">10</div>

  <!-- row 2 -->
  <div class="tile tile--red" style="left:150px;top:398px;width:516px;height:144px"></div>
  <div class="tile tile--numeral tile--framed" style="left:307px;top:396px;width:196px;height:148px">10</div>

  <!-- row 3 -->
  <div class="tile tile--red" style="left:150px;top:556px;width:350px;height:144px"></div>
  <div class="emblem emblem--orbit" role="img" aria-label="Gold emblem with red orbiting ellipses"
       style="left:150px;top:556px;width:160px;height:144px"></div>
  <div class="tile tile--numeral tile--framed" style="left:499px;top:554px;width:168px;height:148px">10</div>

  <!-- row 4 -->
  <div class="tile tile--gold" style="left:310px;top:714px;width:190px;height:144px"></div>
  <div class="tile tile--numeral tile--framed" style="left:148px;top:712px;width:164px;height:148px">10</div>

  <!-- row 5 -->
  <div class="tile tile--red" style="left:310px;top:874px;width:190px;height:142px"></div>
  <div class="tile tile--numeral tile--open" style="left:500px;top:874px;width:166px;height:142px">10</div>
</main>
</body>
</html>
```